We need a label design for our new company called Tovel Crest.
We are a company that is producing Pet Supplements, but the first products launched are going to be for the dogs.
First 3 products that we are launching are:
-Multivitamin (12 in 1)
-Probiotic
-Hip and Joint
We need label design for this three products that are going to be packed in the black plastic jar with the count of 120 pieces in each.
I am uploading our logo, but please do not pay attention to the colors of the logo as that can be changed and adjusted.
- Label dimensions are 2.25" x 11.125"
-Corner radius 0.125

Attached some badges with registrations and approvals.

```html
<!DOCTYPE html>
<html lang="en">
<head>
<meta charset="UTF-8">
<title>Tovel Crest – Dog Supplement Labels</title>
<link href="https://fonts.googleapis.com/css2?family=Poppins:wght@300;400;500;700;800&family=Oswald:wght@400;500&display=swap" rel="stylesheet">
<style>
  :root {
    --page: #ffffff;
    --label-dark: #0d0d0d;
    --label-mid: #2a2a2a;
    --text-light: #f2f2f2;
    --text-soft: #d6d6d6;
    --orange: #f7931e;
    --orange-light: #ffb347;
    --teal: #3fcaa9;
    --teal-light: #7fe0c8;
    --violet: #d88cf2;
    --violet-light: #e9b8fa;
    --chew-text: #2b2b2b;
  }
  * { margin: 0; padding: 0; box-sizing: border-box; }
  html, body {
    width: 1200px; height: 1200px; overflow: hidden;
    background: var(--page);
    font-family: 'Poppins', sans-serif;
  }
  .label-row {
    position: absolute; top: 450px; left: 84px;
    display: flex; gap: 27px;
  }
  .label {
    position: relative; width: 328px; height: 300px;
    border-radius: 12px; overflow: hidden;
    background: linear-gradient(90deg, var(--label-mid) 0%, var(--label-dark) 22%, var(--label-dark) 78%, var(--label-mid) 100%);
    color: var(--text-light);
  }
  .label.probiotic { --accent: var(--orange); --accent-light: var(--orange-light); }
  .label.multivitamin { --accent: var(--teal); --accent-light: var(--teal-light); }
  .label.joint { --accent: var(--violet); --accent-light: var(--violet-light); }

  .brand { position: absolute; left: 60px; top: 28px; display: flex; align-items: center; gap: 8px; }
  .brand-dot { width: 30px; height: 30px; border-radius: 50%; background: var(--accent); }
  .brand-name { font-weight: 700; font-size: 18px; line-height: 1; color: var(--text-light); text-transform: uppercase; }
  .brand-sub { font-weight: 500; font-size: 8.5px; letter-spacing: 0.4px; margin-top: 4px; text-align: center; text-transform: uppercase; }

  .badge { position: absolute; left: 284px; width: 28px; height: 28px; border-radius: 50%;
    background: radial-gradient(circle at 35% 30%, var(--accent-light), var(--accent)); }
  .badge.first { top: 24px; }
  .badge.second { top: 74px; }

  .title { position: absolute; left: 23px; top: 86px; }
  .title-main { font-weight: 400; font-size: 42px; line-height: 1; color: var(--text-light); }
  .title-sub { font-weight: 800; font-size: 35px; line-height: 1.05;
    background: linear-gradient(90deg, var(--accent-light), var(--accent));
    -webkit-background-clip: text; background-clip: text; color: transparent; }
  .multivitamin .title-main, .joint .title-main { font-size: 36px; }
  .multivitamin .title-sub, .joint .title-sub { font-size: 30px; }

  .tag-count { position: absolute; left: 22px; top: 166px; background: var(--text-light); color: #111;
    font-weight: 800; font-style: italic; font-size: 20px; padding: 0 12px; line-height: 24px;
    clip-path: polygon(4% 0, 100% 0, 96% 100%, 0 100%); }
  .ingredients { position: absolute; left: 23px; top: 170px; font-size: 12.5px; font-weight: 400; color: var(--text-soft); }

  .benefits { position: absolute; left: 22px; list-style: none; font-size: 9px; line-height: 12px; color: var(--text-soft); }
  .benefits li::before { content: "•"; margin-right: 8px; font-size: 7px; }
  .probiotic .benefits { top: 180px; }
  .multivitamin .benefits { top: 192px; }
  .joint .benefits { top: 194px; }

  .dog-photo { position: absolute; left: 184px; top: 122px; width: 144px; height: 148px;
    border-radius: 60px 40px 0 0;
    background: radial-gradient(ellipse at 55% 75%, #f4f1ec 0%, #e2d8cc 35%, #b0703c 65%, #5a3a22 100%); }

  .count-tab { position: absolute; left: 18px; top: 239px; height: 22px; padding: 0 28px 0 4px;
    background: linear-gradient(90deg, var(--accent-light), var(--accent));
    clip-path: polygon(0 0, 84% 0, 100% 100%, 0 100%);
    font-family: 'Oswald', sans-serif; font-size: 14px; line-height: 22px; color: var(--chew-text); }
  .count-tab strong { font-weight: 500; }
  .count-tab span { font-weight: 400; }
  .accent-band { position: absolute; left: 0; top: 261px; width: 296px; height: 6px;
    background: linear-gradient(90deg, var(--accent-light), var(--accent)); }
</style>
</head>
<body>
<main class="label-row">
  <section class="label probiotic">
    <div class="brand"><div class="brand-dot"></div><div><div class="brand-name">Tovel Crest</div><div class="brand-sub">Pet Supplements</div></div></div>
    <div class="badge first"></div><div class="badge second"></div>
    <h2 class="title"><div class="title-main">Probiotic</div><div class="title-sub">for Dogs</div></h2>
    <ul class="benefits"><li>High Potency Probiotic</li><li>Support Digestion</li><li>Help Elimination</li><li>Support Intestinal Health</li></ul>
    <div class="dog-photo" role="img" aria-label="Photo of a brown and white terrier puppy peeking over the edge"></div>
    <div class="accent-band"></div>
    <div class="count-tab"><strong>120</strong> <span>SOFT</span> <strong>CHEWS</strong></div>
  </section>

  <section class="label multivitamin">
    <div class="brand"><div class="brand-dot"></div><div><div class="brand-name">Tovel Crest</div><div class="brand-sub">Pet Supplements</div></div></div>
    <div class="badge first"></div><div class="badge second"></div>
    <h2 class="title"><div class="title-main">Multivitamin</div><div class="title-sub">for Dogs</div></h2>
    <div class="tag-count">12-in-1</div>
    <ul class="benefits"><li>Digestion Support</li><li>Immune Support</li><li>Oral Hygenie</li></ul>
    <div class="dog-photo" role="img" aria-label="Photo of a brown and white terrier puppy peeking over the edge"></div>
    <div class="accent-band"></div>
    <div class="count-tab"><strong>120</strong> <span>SOFT</span> <strong>CHEWS</strong></div>
  </section>

  <section class="label joint">
    <div class="brand"><div class="brand-dot"></div><div><div class="brand-name">Tovel Crest</div><div class="brand-sub">Pet Supplements</div></div></div>
    <div class="badge first"></div><div class="badge second"></div>
    <h2 class="title"><div class="title-main">Hip and Joint</div><div class="title-sub">for Dogs</div></h2>
    <div class="ingredients">Glucosamine | MSM | Krill</div>
    <ul class="benefits"><li>Mobility Support</li><li>Maintain Muscles</li><li>Lubricate Joints</li></ul>
    <div class="dog-photo" role="img" aria-label="Photo of a brown and white terrier puppy peeking over the edge"></div>
    <div class="accent-band"></div>
    <div class="count-tab"><strong>120</strong> <span>SOFT</span> <strong>CHEWS</strong></div>
  </section>
</main>
</body>
</html>
```